Dentist Anesthesiologist
BrookMint Dental
Professional
Rafael Okonkwo, DMD, MPH, MBA
418 North Pine Hollow Road
Suite 207915
Phoenix, Arizona 85093
(877) 555-TOOL (8665)
(480) 555-TOOL (8665)
Dr.Okonkwo@BrookMintDental.example
www.BrookMintDental.example
Please visit my website www.BrookMintDental.example for colors (blue and brown). I am not sure if I want my name to be written as Dr. Rafael Okonkwo or Rafael Okonkwo, DMD, MPH, MBA. In the form above, it didn't ask for the business name - it is BrookMint Dental.
I am okay with textual information or the logo design on the back of the card.
Here is the logo design on my website.
Here is the logo design for my website.

```html
<!DOCTYPE html>
<html lang="en">
<head>
<meta charset="utf-8">
<title>BrookMint Dental – Business Card</title>
<link rel="stylesheet" href="https://fonts.googleapis.com/css2?family=Tinos:wght@400;700&display=swap">
<style>
  :root {
    --backdrop: #e6e6e6;
    --card: #ffffff;
    --brand-blue: #3d8cc8;
    --brand-brown: #9a6a3a;
    --ink: #2f3a46;
    --ink-soft: #4a5561;
  }
  * { box-sizing: border-box; margin: 0; padding: 0; }
  html, body { width: 1200px; height: 901px; overflow: hidden; }
  body {
    background: var(--backdrop);
    font-family: "Tinos", "Times New Roman", serif;
    display: flex; flex-direction: column; align-items: center; justify-content: center;
    gap: 40px;
  }
  .card {
    position: relative;
    width: 700px; height: 400px;
    background: var(--card);
    border-radius: 22px;
    box-shadow: 0 4px 16px rgba(0,0,0,.12);
  }
  .brand {
    display: flex; align-items: center; gap: 12px;
  }
  .brand-mark {
    flex: none; border-radius: 50%; background: var(--brand-blue);
  }
  .brand-name {
    color: var(--brand-blue);
    font-weight: 400;
    white-space: nowrap;
    line-height: 1;
  }
  /* front */
  .card-front .brand {
    position: absolute; left: 0; right: 0; top: 172px; justify-content: center;
  }
  .card-front .brand-mark { width: 26px; height: 26px; }
  .card-front .brand-name { font-size: 46px; }
  /* back */
  .card-back .brand { position: absolute; left: 40px; top: 42px; gap: 10px; }
  .card-back .brand-mark { width: 20px; height: 20px; }
  .card-back .brand-name { font-size: 34px; }
  .contact {
    position: absolute; left: 392px; top: 128px;
    color: var(--ink); font-size: 14px; line-height: 1.22;
  }
  .contact .name { font-weight: 700; color: var(--ink-soft); }
  .contact .role { margin-bottom: 14px; }
  .contact .address { margin-bottom: 12px; }
  .contact-lines { list-style: none; }
  .contact-lines li { display: flex; align-items: center; gap: 8px; }
  .contact-lines svg { width: 12px; height: 12px; fill: var(--brand-brown); flex: none; }
  .website {
    position: absolute; right: 34px; bottom: 28px;
    font-size: 17px; color: var(--ink); letter-spacing: .3px;
  }
  .website .domain { color: var(--brand-blue); font-weight: 700; }
</style>
</head>
<body>
  <section class="card card-front">
    <div class="brand">
      <span class="brand-mark"></span>
      <span class="brand-name">BrookMint Dental</span>
    </div>
  </section>

  <section class="card card-back">
    <div class="brand">
      <span class="brand-mark"></span>
      <span class="brand-name">BrookMint Dental</span>
    </div>
    <div class="contact">
      <div class="name">Rafael Okonkwo, DMD, MPH, MBA</div>
      <div class="role">Dentist Anesthesiologist</div>
      <div class="address">418 North Pine Hollow Road<br>Suite 207915<br>Phoenix, Arizona 85093</div>
      <ul class="contact-lines">
        <li><svg viewBox="0 0 12 12"><path d="M2 1h3l1 3-2 1a7 7 0 0 0 3 3l1-2 3 1v3a1 1 0 0 1-1 1A10 10 0 0 1 1 2a1 1 0 0 1 1-1z"/></svg>(877) 555-TOOL (8665)</li>
        <li><svg viewBox="0 0 12 12"><path d="M2 1h3l1 3-2 1a7 7 0 0 0 3 3l1-2 3 1v3a1 1 0 0 1-1 1A10 10 0 0 1 1 2a1 1 0 0 1 1-1z"/></svg>(480) 555-TOOL (8665)</li>
        <li><svg viewBox="0 0 12 12"><path d="M3 1h6v3H3zM1 5h10v5H1zM3 8h6v3H3z"/></svg>(480) 555-TOOL (8665)</li>
        <li><svg viewBox="0 0 12 12"><path d="M3 0h6a1 1 0 0 1 1 1v10a1 1 0 0 1-1 1H3a1 1 0 0 1-1-1V1a1 1 0 0 1 1-1zm0 2v7h6V2z"/></svg>(888) 555-0142</li>
        <li><svg viewBox="0 0 12 12"><path d="M0 2h12v8H0zm1 1v.5l5 3 5-3V3z"/></svg>Dr.Okonkwo@BrookMintDental.example</li>
      </ul>
    </div>
    <div class="website">www.<span class="domain">BrookMintDental</span>.example</div>
  </section>
</body>
</html>
```